VoyaPoint

1. We need a four color business card
2. The Front of card needs to include our Logo, Slogan which is "Launching, Expanding & Optimizing Organizations, Individual Name, email, two phone numbers, email, skype address, website address
3. Back of card needs to include the following topics: Start Ups & Business Optimization,Product Acquisition, Destination Product Marketing & Representation,Marketing & Sales, Operations, Training/Education, Digital Marketing, Keynote Addresses/Public Speaking
3. Back of card can not be black as it needs to be a color that people can write on
Industry/Entity Type
Business

```html
<!DOCTYPE html>
<html lang="en">
<head>
<meta charset="utf-8">
<title>VoyaPoint – Business Card</title>
<link rel="stylesheet" href="https://fonts.googleapis.com/css2?family=Questrial&family=Archivo+Narrow:wght@700&display=swap">
<style>
  :root {
    --bg: #e9e6e1;
    --paper: #ffffff;
    --ink-dark: #101215;
    --ink-dark-2: #1d2127;
    --blue: #1f5fa9;
    --green: #7fb342;
    --orange: #f0901f;
    --grey: #6c6f73;
    --faint: #eef0f2;
  }
  * { box-sizing: border-box; margin: 0; padding: 0; }
  html, body { width: 1200px; height: 784px; overflow: hidden; }
  body {
    background: var(--bg);
    font-family: "Questrial", "Century Gothic", sans-serif;
    position: relative;
  }
  .card {
    position: absolute;
    width: 540px;
    height: 309px;
    background: var(--paper);
    box-shadow: 0 6px 18px rgba(0,0,0,.18);
    overflow: hidden;
  }
  /* Back: services list */
  .card--back { left: 30px; top: 237px; }
  .services {
    list-style: none;
    position: absolute;
    left: 34px;
    top: 40px;
    font-family: "Archivo Narrow", "Arial Narrow", sans-serif;
    font-weight: 700;
    font-size: 14px;
    text-transform: uppercase;
    letter-spacing: .2px;
    line-height: 28.5px;
  }
  .services .blue { color: var(--blue); }
  .services .green { color: var(--green); }
  .services .orange { color: var(--orange); }
  .services li:nth-child(2) { padding-left: 6px; }
  .services li:nth-child(3) { padding-left: 12px; }
  .services li:nth-child(4) { padding-left: 18px; }
  .services li:nth-child(5) { padding-left: 24px; }
  .services li:nth-child(6) { padding-left: 30px; }
  .services li:nth-child(7) { padding-left: 36px; }
  .services li:nth-child(8) { padding-left: 42px; }
  .back-disc {
    position: absolute;
    right: 40px;
    top: 10px;
    width: 170px;
    height: 170px;
    border-radius: 50%;
    background: var(--faint);
  }

  /* Front: identity */
  .card--front { left: 630px; top: 237px; }
  .front-top { position: absolute; inset: 0 0 auto 0; height: 128px; background: var(--paper); }
  .brand {
    position: absolute;
    left: 34px;
    top: 30px;
    display: flex;
    align-items: center;
    gap: 14px;
  }
  .brand-dot {
    width: 52px; height: 52px;
    border-radius: 50%;
    background: var(--blue);
  }
  .brand-name {
    font-size: 44px;
    color: var(--blue);
    line-height: 1;
    letter-spacing: -.5px;
  }
  .slogan {
    position: absolute;
    left: 100px;
    top: 96px;
    width: 400px;
    border-top: 1px solid #b9bcc0;
    padding-top: 4px;
    font-size: 10.5px;
    letter-spacing: .8px;
    font-variant: small-caps;
    color: var(--grey);
  }
  .front-stripe {
    position: absolute; left: 0; right: 0; top: 128px; height: 6px;
    background: var(--blue);
  }
  .front-panel {
    position: absolute; left: 0; right: 0; top: 134px; bottom: 0;
    background: linear-gradient(180deg, var(--ink-dark-2), var(--ink-dark));
  }
  .person { position: absolute; left: 40px; top: 16px; }
  .person-name { font-size: 19px; color: var(--blue); line-height: 1.1; }
  .person-title { font-size: 13px; color: var(--green); margin-left: 6px; }
  .contacts {
    list-style: none;
    position: absolute;
    left: 40px;
    top: 64px;
    font-size: 16px;
    color: var(--orange);
    line-height: 20px;
  }
  .contacts li { display: flex; align-items: center; gap: 6px; }
  .contacts svg { width: 14px; height: 14px; flex: none; }
</style>
</head>
<body>

<section class="card card--back" aria-label="Card back: services">
  <div class="back-disc"></div>
  <ul class="services">
    <li class="blue">Start Ups &amp; Business Optimization</li>
    <li class="green">Product Acquisition</li>
    <li class="orange">Destination Product Marketing &amp; Representation</li>
    <li class="blue">Marketing &amp; Sales</li>
    <li class="green">Operations</li>
    <li class="orange">Training/Education</li>
    <li class="blue">Digital Marketing</li>
    <li class="green">Keynote Addresses/Public Speaking</li>
  </ul>
</section>

<section class="card card--front" aria-label="Card front: contact">
  <div class="front-top">
    <div class="brand">
      <span class="brand-dot"></span>
      <span class="brand-name">VoyaPoint</span>
    </div>
    <p class="slogan">Launching, Expanding &amp; Optimizing Organizations</p>
  </div>
  <div class="front-stripe"></div>
  <div class="front-panel">
    <div class="person">
      <p class="person-name">Dana Whitfield</p>
      <p class="person-title">President</p>
    </div>
    <ul class="contacts">
      <li>
        <svg viewBox="0 0 16 16"><path fill="#2a7fd4" d="M3 1l3 3-1.5 2a9 9 0 0 0 5.5 5.5L12 10l3 3-2 2C7 15 1 9 1 3z"/></svg>
        (555)240-7318
      </li>
      <li>
        <svg viewBox="0 0 16 16"><path fill="#2a7fd4" d="M3 1l3 3-1.5 2a9 9 0 0 0 5.5 5.5L12 10l3 3-2 2C7 15 1 9 1 3z"/></svg>
        (555)240-9162
      </li>
      <li>
        <svg viewBox="0 0 16 16"><rect x="1" y="3" width="14" height="10" rx="1.5" fill="#2a7fd4"/><path d="M1.5 4L8 9l6.5-5" stroke="#101215" stroke-width="1.3" fill="none"/></svg>
        dana@voyapoint.com
      </li>
      <li>
        <svg viewBox="0 0 16 16"><g fill="none" stroke="#2a7fd4" stroke-width="1.3"><circle cx="8" cy="8" r="6.5"/><ellipse cx="8" cy="8" rx="3" ry="6.5"/><path d="M1.5 8h13M2.5 4.5h11M2.5 11.5h11"/></g></svg>
        www.voyapoint.com
      </li>
      <li>
        <svg viewBox="0 0 16 16"><circle cx="8" cy="8" r="7" fill="#2a7fd4"/></svg>
        dana_voyapoint
      </li>
    </ul>
  </div>
</section>

</body>
</html>
```